International Flower distributer needs a landing page

We are looking to have a landing page made that will be easy to maintain and upload more content as our business grows.

We like the template designs and ease of use of Pagewright. We'd explore other host sites.

Hello,

To start we would like something that can be managed and updated on a platform like pagewright. We like page wright because of the premade designs and flexibility.

Website requirements:

- About us:

- Marlowe Vantage Corp - Established 1999

- Verna Holt - Founder

- Danielle Holt - Account Executive

- Gregory Holt - Director of Operations

- Pilar Wendham - (Jo's Job Description?)

- Renata Valcourt (Make us look like a bigger company with more staff)

What we do:

- Personalized Customer service

- Exclusively Mass market experience to meet high demands

- Dedicated team assigned to your account

How we do it:

- Partnerships with farms in COlombia, ecuador and costa rica

- Farm fresh delivered directly from cargo planes to state of the art cooler facility at Delmont Airport

- Verity Trust?

Products we Sell:

- Farm made bouquets

- Consumer Bunches

- Programs Tailored to fit customer's retail program

For more Information:

- Gregory and Danielle phone and email

- Submit email inquiry

Gathering more feedback

Corporate buyers that want to verify who we are and get our contact information

Floral, but not a flower shop. We import farm fresh cut flowers from south america and send them directly to supermarkets around the country.

• We are not selling anything on the website. We sell business to business.

```html
<!DOCTYPE html>
<html lang="en">
<head>
<meta charset="utf-8">
<title>Marlowe Vantage – Farm Fresh Cut Flowers</title>
<link href="https://fonts.googleapis.com/css2?family=Archivo:wght@700;800&family=Mulish:wght@400;600;700&display=swap" rel="stylesheet">
<style>
:root{
  --navy:#231d7d;
  --green:#76bc2a;
  --orange:#f2831a;
  --ink:#2b2b35;
  --grey-bg:#f1f2f4;
  --white:#ffffff;
}
*{box-sizing:border-box;margin:0;padding:0}
html,body{width:1200px;height:3515px;overflow:hidden}
body{position:relative;background:var(--white);font-family:"Mulish",sans-serif;color:var(--ink)}
.abs{position:absolute}
.heading{font-family:"Archivo",sans-serif;font-weight:800;color:var(--navy);text-transform:uppercase;letter-spacing:.3px}
.btn{position:absolute;display:flex;align-items:center;justify-content:center;background:var(--orange);color:var(--white);font-family:"Archivo",sans-serif;font-weight:700;font-size:14px;border-radius:26px;text-transform:uppercase;letter-spacing:.3px}

/* Hero */
.hero{left:0;top:0;width:1200px;height:720px;background:linear-gradient(100deg,#eef5dc 0%,#dcebb8 30%,#b9d48a 48%,#e9a6c4 62%,#c14f8e 78%,#7d2a6a 92%,#5a8d3a 100%)}
.brand{left:112px;top:14px;display:flex;align-items:center;gap:12px}
.brand-dot{width:70px;height:70px;border-radius:50%;background:var(--navy)}
.brand-name{font-family:"Archivo",sans-serif;font-weight:800;font-size:26px;line-height:26px;color:var(--navy);text-transform:uppercase}
.nav{left:427px;top:44px;display:flex;gap:25px;font-family:"Archivo",sans-serif;font-weight:700;font-size:14px;color:#1d1d2a;text-transform:uppercase}
.nav .active{color:var(--orange);border-bottom:2px solid var(--orange);padding-bottom:8px}
.hero-title{left:112px;top:255px;font-size:36px}
.hero-title .lead{color:var(--green)}
.hero-text{left:112px;top:310px;width:560px;font-size:16.5px;line-height:27px;font-weight:600;color:#2a2a2a}
.dots{left:112px;top:523px;display:flex;gap:3px}
.dots span{width:16px;height:16px;border-radius:50%;border:2px solid var(--white)}
.dots .on{background:var(--white)}

/* About */
.about{left:0;top:720px;width:1200px;height:570px;background:linear-gradient(180deg,#ffffff 0%,#f3f7ef 45%,#f6eef2 80%,#eef3e6 100%)}
.about-photo{left:127px;top:752px;width:440px;height:440px;border-radius:50%;background:radial-gradient(circle at 45% 55%,#b8a6e8 0%,#6c7bd6 30%,#e58fb4 55%,#4a3b6f 85%);border:6px solid var(--white);box-shadow:-14px 0 0 0 var(--navy)}
.about-title{left:638px;top:785px;font-size:36px}
.about-copy{left:638px;top:858px;width:451px;font-size:14.5px;line-height:26px;color:#3a3a3a;text-align:justify}
.about-copy p+p{margin-top:15px}

/* What we do */
.what{left:0;top:1290px;width:566px;height:472px;background:var(--green)}
.what-photo{left:566px;top:1290px;width:634px;height:472px;background:radial-gradient(circle at 60% 45%,#e2455a 0%,#b52a3c 30%,#5b3a2e 65%,#2b2e20 100%)}
.what-title{left:112px;top:1343px;font-size:29px;color:var(--white)}
.feature{left:112px;display:flex;align-items:center;gap:33px;width:420px}
.feature-icon{flex:none;width:86px;height:86px;border-radius:50%;background:var(--white);display:flex;align-items:center;justify-content:center;box-shadow:0 4px 10px rgba(0,0,0,.12)}
.feature-text{font-size:15.5px;line-height:27px;font-weight:600;color:var(--white)}

/* How */
.how{left:0;top:1762px;width:1200px;height:515px;background:var(--grey-bg)}
.how-frame{left:112px;top:1838px;width:472px;height:358px;border:7px solid var(--green);border-right:none;border-bottom:none;border-radius:16px 0 0 16px}
.how-photo{left:128px;top:1856px;width:472px;height:343px;border-radius:10px;background:linear-gradient(160deg,#cfd8c6 0%,#8bb07a 35%,#d95c78 60%,#4f7a3b 100%)}
.how-title{left:644px;top:1866px;font-size:34px}
.how-list{left:644px;top:1932px;width:445px;list-style:none;font-size:14.5px;line-height:26px;color:#3a3a3a}
.how-list li{display:flex;gap:22px;margin-bottom:9px}
.how-list svg{flex:none;margin-top:5px}

/* Products */
.products-title{left:0;top:2362px;width:1200px;text-align:center;font-size:34px}
.card{border-radius:14px;display:flex;align-items:flex-end;justify-content:center;text-align:center;color:var(--white);font-family:"Archivo",sans-serif;font-weight:700;font-size:20px;line-height:29px;text-transform:uppercase}
.card-programs{left:112px;top:2446px;width:565px;height:257px;padding-bottom:22px;background:linear-gradient(160deg,#1c2a1d 0%,#33492e 55%,#16201a 100%)}
.card-bunches{left:112px;top:2729px;width:565px;height:257px;padding-bottom:20px;background:linear-gradient(150deg,#3f3b35 0%,#8e7a61 50%,#c9463a 70%,#3a342c 100%)}
.card-bouquets{left:703px;top:2446px;width:386px;height:540px;padding-bottom:24px;background:linear-gradient(170deg,#3f6a34 0%,#2d4a2b 45%,#b7336b 68%,#22301f 100%)}

/* Footer */
.footer-band{left:0;top:3040px;width:1200px;height:475px}
.footer-col{top:3256px;color:var(--white);font-size:12px}
.footer-col h4{font-family:"Mulish",sans-serif;font-weight:700;font-size:13.5px;margin-bottom:16px}
.footer-col li{list-style:none;display:flex;gap:14px;line-height:24px}
.footer-col .contact li{align-items:flex-start}
.footer-col .contact li span{line-height:22px}
.inquiry{left:569px;width:310px}
.inquiry p{line-height:24px}
.email-field{margin-top:14px;width:314px;height:46px;border-radius:23px;background:var(--white);display:flex;overflow:hidden}
.email-field span{flex:1;padding-left:16px;display:flex;align-items:center;color:#444;font-size:11.5px}
.email-field b{width:46px;background:var(--orange);display:flex;align-items:center;justify-content:center}
.footer-mark{left:941px;top:3263px;width:150px;height:150px;border-radius:50%;border:3px solid var(--white);display:flex;align-items:center;justify-content:center;text-align:center;color:var(--white);font-family:"Archivo",sans-serif;font-weight:800;font-size:17px;line-height:21px;text-transform:uppercase}
.footer-rule{left:112px;top:3455px;width:977px;height:1px;background:rgba(255,255,255,.35)}
.copyright{left:0;top:3478px;width:1200px;text-align:center;color:var(--white);font-size:12px}
.socials{left:998px;top:3482px;display:flex;gap:12px}
.socials span{width:12px;height:12px;border-radius:50%;background:var(--white)}
.chat{left:1118px;top:3414px;width:46px;height:46px;border-radius:50%;background:var(--white);display:flex;align-items:center;justify-content:center;box-shadow:0 2px 8px rgba(0,0,0,.25)}
</style>
</head>
<body>

<!-- Hero -->
<section class="abs hero" role="img" aria-label="Close-up photograph of pink and purple tulips on a soft green blurred background"></section>
<div class="abs brand"><span class="brand-dot"></span><span class="brand-name">Marlowe<br>Vantage</span></div>
<nav class="abs nav">
  <span class="active">Home</span><span>About Us</span><span>What We Do</span><span>How We Do It</span><span>Products We Sell</span><span>Contact</span>
</nav>
<h1 class="abs heading hero-title"><span class="lead">Welcome to</span> Marlowe Vantage</h1>
<p class="abs hero-text">Sed ut perspiciatis unde omnis iste natus error sit voluptatem accusantium doloremque laudantiu.</p>
<span class="btn" style="left:112px;top:390px;width:154px;height:47px">Get Started</span>
<div class="abs dots"><span></span><span class="on"></span><span></span><span></span></div>

<svg class="abs" style="left:0;top:540px" width="1200" height="200" viewBox="0 540 1200 200">
  <path d="M0,628 C160,552 330,540 520,600 C700,660 860,740 1200,628 L1200,740 L0,740 Z" fill="var(--green)"/>
  <path d="M0,632 C160,562 330,552 520,612 C700,670 860,726 1200,648 L1200,740 L0,740 Z" fill="var(--white)"/>
</svg>
<div class="abs" style="left:562px;top:608px;width:76px;height:76px;border-radius:50%;background:var(--white);box-shadow:0 3px 10px rgba(0,0,0,.18);display:flex;align-items:center;justify-content:center">
  <svg width="34" height="34" viewBox="0 0 34 34"><circle cx="17" cy="17" r="12" fill="none" stroke="var(--navy)" stroke-width="2.5"/><circle cx="17" cy="17" r="4" fill="var(--green)"/></svg>
</div>

<!-- About -->
<section class="abs about" role="img" aria-label="Faint field of wildflowers as background"></section>
<div class="abs about-photo" role="img" aria-label="Photograph of hands arranging a bouquet of pink roses and blue hydrangeas"></div>
<h2 class="abs heading about-title">About Us</h2>
<div class="abs about-copy">
  <p>At vero eos et accusamus et iusto odio dignissimos ducimus qui blanditiis praesentium voluptatum deleniti atque corrupti quos dolores et quas molestias excepturi sint occaecati cupiditate non provident, similique sunt in culpa.</p>
  <p>Et harum quidem rerum facilis est et expedita distinctio. Nam libero tempore, cum soluta nobis est eligendi optio cumque nihil impedit quo minus id quod maxime placeat.</p>
</div>
<span class="btn" style="left:638px;top:1093px;width:155px;height:49px">Learn More</span>

<!-- What we do -->
<section class="abs what"></section>
<div class="abs what-photo" role="img" aria-label="Photograph of red peonies in a glass vase"></div>
<h2 class="abs heading what-title">What We Do</h2>
<div class="abs feature" style="top:1412px">
  <span class="feature-icon"><svg width="40" height="40" viewBox="0 0 40 40" fill="none" stroke="var(--navy)" stroke-width="2"><circle cx="20" cy="10" r="4"/><path d="M13 22c0-4 3-6 7-6s7 2 7 6"/><path d="M4 18v10l8 6h6M36 18v10l-8 6h-6"/></svg></span>
  <span class="feature-text">Personalized Customer service</span>
</div>
<div class="abs feature" style="top:1515px">
  <span class="feature-icon"><svg width="40" height="40" viewBox="0 0 40 40" fill="none" stroke="var(--navy)" stroke-width="2"><path d="M6 16h28l-3-8H9z"/><path d="M8 16v18h24V16"/><rect x="13" y="22" width="7" height="12"/><rect x="23" y="22" width="6" height="6"/></svg></span>
  <span class="feature-text">Exclusively Mass market experience to meet high demands</span>
</div>
<div class="abs feature" style="top:1618px">
  <span class="feature-icon"><svg width="40" height="40" viewBox="0 0 40 40" fill="none" stroke="var(--navy)" stroke-width="2"><circle cx="20" cy="20" r="5"/><circle cx="20" cy="6" r="3"/><circle cx="20" cy="34" r="3"/><circle cx="6" cy="20" r="3"/><circle cx="34" cy="20" r="3"/><path d="M20 9v6M20 25v6M9 20h6M25 20h6"/></svg></span>
  <span class="feature-text">Dedicated team assigned to your account</span>
</div>

<!-- How we do it -->
<section class="abs how"></section>
<div class="abs how-frame"></div>
<div class="abs how-photo" role="img" aria-label="Photograph of a grower tending roses in a greenhouse"></div>
<h2 class="abs heading how-title">How We Do It</h2>
<ul class="abs how-list">
  <li><svg width="14" height="14" viewBox="0 0 14 14"><circle cx="7" cy="7" r="7" fill="var(--green)"/><path d="M4 7h6M7.5 4.5 10 7l-2.5 2.5" stroke="#fff" stroke-width="1.6" fill="none"/></svg><span>Partnerships with farms in COlombia, ecuador and costa rica</span></li>
  <li><svg width="14" height="14" viewBox="0 0 14 14"><circle cx="7" cy="7" r="7" fill="var(--green)"/><path d="M4 7h6M7.5 4.5 10 7l-2.5 2.5" stroke="#fff" stroke-width="1.6" fill="none"/></svg><span>Farm fresh delivered directly from cargo planes to state of the art cooler facility at Delmont Airport</span></li>
  <li><svg width="14" height="14" viewBox="0 0 14 14"><circle cx="7" cy="7" r="7" fill="var(--green)"/><path d="M4 7h6M7.5 4.5 10 7l-2.5 2.5" stroke="#fff" stroke-width="1.6" fill="none"/></svg><span>Verity Trust?</span></li>
</ul>
<span class="btn" style="left:644px;top:2112px;width:155px;height:50px">Learn More</span>

<!-- Products -->
<h2 class="abs heading products-title">Products We Sell</h2>
<div class="abs card card-programs" role="img" aria-label="Photograph of white blossoms on dark foliage"><span>Programs Tailored<br>to fit customer's retail program</span></div>
<div class="abs card card-bunches" role="img" aria-label="Photograph of tulips being wrapped in kraft paper"><span>Consumer Bunches</span></div>
<div class="abs card card-bouquets" role="img" aria-label="Photograph of a grower cutting pink flowers in a garden"><span>Farm<br>Made Bouquets</span></div>

<!-- Footer -->
<svg class="abs footer-band" width="1200" height="475" viewBox="0 3040 1200 475">
  <path d="M0,3180 C120,3110 240,3060 380,3068 C600,3080 780,3240 960,3238 C1080,3236 1150,3200 1200,3180 L1200,3515 L0,3515 Z" fill="var(--green)"/>
  <path d="M0,3192 C120,3126 240,3080 380,3088 C600,3100 780,3226 960,3224 C1080,3222 1150,3198 1200,3186 L1200,3515 L0,3515 Z" fill="var(--navy)"/>
</svg>

<div class="abs footer-col" style="left:112px">
  <h4>Quick Links</h4>
  <ul>
    <li><svg width="11" height="11" viewBox="0 0 14 14" style="margin-top:7px"><circle cx="7" cy="7" r="7" fill="var(--green)"/><path d="M4 7h6M7.5 4.5 10 7l-2.5 2.5" stroke="#fff" stroke-width="1.6" fill="none"/></svg>Home</li>
    <li><svg width="11" height="11" viewBox="0 0 14 14" style="margin-top:7px"><circle cx="7" cy="7" r="7" fill="var(--green)"/><path d="M4 7h6M7.5 4.5 10 7l-2.5 2.5" stroke="#fff" stroke-width="1.6" fill="none"/></svg>About Us</li>
    <li><svg width="11" height="11" viewBox="0 0 14 14" style="margin-top:7px"><circle cx="7" cy="7" r="7" fill="var(--green)"/><path d="M4 7h6M7.5 4.5 10 7l-2.5 2.5" stroke="#fff" stroke-width="1.6" fill="none"/></svg>What We Do</li>
    <li><svg width="11" height="11" viewBox="0 0 14 14" style="margin-top:7px"><circle cx="7" cy="7" r="7" fill="var(--green)"/><path d="M4 7h6M7.5 4.5 10 7l-2.5 2.5" stroke="#fff" stroke-width="1.6" fill="none"/></svg>How We Do It</li>
    <li><svg width="11" height="11" viewBox="0 0 14 14" style="margin-top:7px"><circle cx="7" cy="7" r="7" fill="var(--green)"/><path d="M4 7h6M7.5 4.5 10 7l-2.5 2.5" stroke="#fff" stroke-width="1.6" fill="none"/></svg>Products We Sell</li>
    <li><svg width="11" height="11" viewBox="0 0 14 14" style="margin-top:7px"><circle cx="7" cy="7" r="7" fill="var(--green)"/><path d="M4 7h6M7.5 4.5 10 7l-2.5 2.5" stroke="#fff" stroke-width="1.6" fill="none"/></svg>Contact</li>
  </ul>
</div>

<div class="abs footer-col" style="left:310px">
  <h4>Contact</h4>
  <ul class="contact">
    <li><svg width="10" height="12" viewBox="0 0 10 12" style="margin-top:5px"><path d="M5 0a4 4 0 0 1 4 4c0 3-4 8-4 8S1 7 1 4a4 4 0 0 1 4-4z" fill="var(--green)"/><circle cx="5" cy="4" r="1.5" fill="var(--navy)"/></svg><span>1820 Harbor Loop Drive<br>Delmont, FL 33990</span></li>
    <li><svg width="11" height="11" viewBox="0 0 12 12" style="margin-top:5px"><path d="M2 1l2.5 0 1 3-1.5 1a7 7 0 0 0 3 3l1-1.5 3 1V11C6 11 1 6 1 1z" fill="var(--green)"/></svg><span>555-014-2761</span></li>
    <li><svg width="11" height="11" viewBox="0 0 12 12" style="margin-top:5px"><path d="M2 1l2.5 0 1 3-1.5 1a7 7 0 0 0 3 3l1-1.5 3 1V11C6 11 1 6 1 1z" fill="var(--green)"/></svg><span>555-019-4830</span></li>
    <li><svg width="11" height="9" viewBox="0 0 12 9" style="margin-top:6px"><rect width="12" height="9" rx="1" fill="var(--green)"/><path d="M0 1l6 4 6-4" stroke="var(--navy)" fill="none"/></svg><span>Gregory@marlowevantagecorp.example</span></li>
    <li><svg width="11" height="9" viewBox="0 0 12 9" style="margin-top:6px"><rect width="12" height="9" rx="1" fill="var(--green)"/><path d="M0 1l6 4 6-4" stroke="var(--navy)" fill="none"/></svg><span>Danielle@marlowevantagecorp.example</span></li>
  </ul>
</div>

<div class="abs footer-col inquiry">
  <h4>Submit Email Inquiry</h4>
  <p>Subscribe to our mailing list to receives daily updates direct to your inbox!</p>
  <div class="email-field"><span>Email Address</span><b><svg width="16" height="16" viewBox="0 0 16 16"><path d="M1 8 15 1 11 15 8 9z" fill="none" stroke="#fff" stroke-width="1.5" stroke-linejoin="round"/></svg></b></div>
</div>

<div class="abs footer-mark">Marlowe<br>Vantage</div>

<div class="abs footer-rule"></div>
<p class="abs copyright">© 2022 <b>MARLOWE VANTAGE.</b> All Rights Reserved</p>
<div class="abs socials" aria-label="Social profiles"><span></span><span></span><span></span><span></span></div>
<div class="abs chat"><svg width="22" height="20" viewBox="0 0 22 20"><path d="M2 2h18v11H9l-5 4v-4H2z" fill="var(--orange)"/></svg></div>

</body>
</html>
```